Buch-/eBook-Cover für Hersteller von Papierprodukten
Zielgruppe
Hersteller von Pierprodukten. Hier Collegeblöcke für Teens zwischen 11 und 17 Jahren im Fokus
Aufgabenstellung
modern, stilsicher, farbig, auch pastell, trendgerecht: Thema Natürlichkeit im 'DopaminStil' interpretiert

```html
<!DOCTYPE html>
<html lang="de">
<head>
<meta charset="utf-8">
<title>Flora Vibes – Collegeblock Cover</title>
<link href="https://fonts.googleapis.com/css2?family=Fira+Sans+Condensed:wght@600&display=swap" rel="stylesheet">
<style>
  :root {
    --page: #ffffff;
    --title-yellow: #f4e41c;
    --tag-white: #ffffff;
    --edition-blue: #2f86d6;
    --corner-purple: #4b3a6e;
    --grid-line: #b9b9c4;
    --grid-paper: #ffffff;
    --coral: #f06a6e;
    --orange: #f7943a;
    --teal: #2aa3a6;
    --magenta: #d8338a;
    --violet: #6a2f8c;
    --night: #1b1f4a;
    --deep-teal: #0f5f66;
    --pink: #e8438f;
    --gold: #f7c12b;
  }
  * { box-sizing: border-box; margin: 0; padding: 0; }
  html, body { width: 892px; height: 1200px; overflow: hidden; background: var(--page); }
  .sheet { position: relative; width: 892px; height: 1200px; }
  .cover {
    position: absolute;
    left: 288px;
    width: 316px;
    height: 446px;
    overflow: hidden;
  }
  .cover--coral { top: 119px; }
  .cover--night { top: 632px; }
  .cover-art { position: absolute; inset: 0; }
  .cover--coral .cover-art {
    background:
      radial-gradient(circle at 15% 12%, var(--teal) 0 16%, transparent 32%),
      radial-gradient(circle at 80% 10%, var(--orange) 0 10%, transparent 26%),
      radial-gradient(circle at 90% 40%, var(--violet) 0 12%, transparent 30%),
      radial-gradient(circle at 65% 82%, var(--deep-teal) 0 18%, transparent 36%),
      radial-gradient(circle at 20% 78%, var(--teal) 0 10%, transparent 28%),
      radial-gradient(circle at 55% 30%, var(--orange) 0 12%, transparent 30%),
      linear-gradient(160deg, var(--coral), var(--magenta) 70%, var(--violet));
  }
  .cover--night .cover-art {
    background:
      radial-gradient(circle at 70% 10%, var(--gold) 0 6%, transparent 20%),
      radial-gradient(circle at 20% 15%, var(--teal) 0 10%, transparent 28%),
      radial-gradient(circle at 45% 63%, var(--gold) 0 7%, transparent 20%),
      radial-gradient(circle at 25% 80%, var(--pink) 0 8%, transparent 24%),
      radial-gradient(circle at 70% 85%, var(--teal) 0 14%, transparent 32%),
      radial-gradient(circle at 60% 45%, var(--magenta) 0 6%, transparent 22%),
      linear-gradient(170deg, var(--night), #24295e 60%, var(--night));
  }
  .name-line {
    position: absolute;
    left: 57px;
    font-family: "Fira Sans Condensed", sans-serif;
    font-weight: 600;
    color: var(--title-yellow);
    font-size: 54px;
    line-height: 54px;
    letter-spacing: 0.5px;
    white-space: nowrap;
  }
  .name-line--top { top: 152px; }
  .name-line--bottom { top: 207px; }
  .hashtag {
    position: absolute;
    left: 59px;
    top: 199px;
    font-family: "Fira Sans Condensed", sans-serif;
    font-weight: 600;
    font-size: 10.5px;
    line-height: 12px;
    color: var(--tag-white);
  }
  .edition {
    position: absolute;
    left: 58px;
    top: 413px;
    font-family: "Fira Sans Condensed", sans-serif;
    font-weight: 600;
    font-size: 10px;
    letter-spacing: 0.2px;
    color: var(--edition-blue);
  }
  .page-corner { position: absolute; right: 0; bottom: 0; width: 76px; height: 36px; }
</style>
</head>
<body>
<main class="sheet">
  <section class="cover cover--coral">
    <div class="cover-art" role="img" aria-label="Tropische Collage mit Papagei, Hibiskusblüten und Monstera-Blättern in Koralle, Orange und Türkis"></div>
    <h1 class="product-name">
      <span class="name-line name-line--top">FLORA</span>
      <span class="name-line name-line--bottom">VIBES</span>
    </h1>
    <p class="hashtag">#shineyourway</p>
    <p class="edition">LIMITED EDITION</p>
    <svg class="page-corner" viewBox="0 0 76 36" aria-hidden="true">
      <defs>
        <pattern id="grid-a" width="5" height="5" patternUnits="userSpaceOnUse">
          <path d="M5 0H0V5" fill="none" stroke="var(--grid-line)" stroke-width="0.5"/>
        </pattern>
      </defs>
      <polygon points="0,36 76,0 76,36" fill="var(--grid-paper)"/>
      <polygon points="0,36 76,0 76,36" fill="url(#grid-a)"/>
      <polygon points="30,36 76,14 76,36" fill="var(--corner-purple)"/>
    </svg>
  </section>

  <section class="cover cover--night">
    <div class="cover-art" role="img" aria-label="Nächtlicher Dschungel mit pinken und gelben Blüten zwischen türkisen Palmblättern"></div>
    <h1 class="product-name">
      <span class="name-line name-line--top">FLORA</span>
      <span class="name-line name-line--bottom">VIBES</span>
    </h1>
    <p class="hashtag">#shineyourway</p>
    <p class="edition">LIMITED EDITION</p>
    <svg class="page-corner" viewBox="0 0 76 36" aria-hidden="true">
      <defs>
        <pattern id="grid-b" width="5" height="5" patternUnits="userSpaceOnUse">
          <path d="M5 0H0V5" fill="none" stroke="var(--grid-line)" stroke-width="0.5"/>
        </pattern>
      </defs>
      <polygon points="0,36 76,0 76,36" fill="var(--grid-paper)"/>
      <polygon points="0,36 76,0 76,36" fill="url(#grid-b)"/>
      <polygon points="30,36 76,14 76,36" fill="var(--corner-purple)"/>
    </svg>
  </section>
</main>
</body>
</html>
```